5 Banner für die Startseite der Hompage
Zielgruppe
Wir sind eine 'kreative' kleine Truppe, die mit neuen Ideen versuchen wollen, auch mal andere Wege in den Projekten zu gehen.
unsere neue Webseite lautet
Aufgabenstellung
Auf meiner Webseite www.quarvelon.de habe ich bereits einen ersten Vorschlag eingefügt.
Es geht um die 5 Banner auf der Startseite; diese sollen sowohl Designtechnisch als auch optisch sehr ansprechend wirken, um das Interesse potentieller Kunden zu wecken.
Meine Farben habe ich mit angehängt.
Der Text könnte sich noch anpassen, muss aber mit in den Banner aufgenommen werden.
Breite sollte 1200Pixel; Höhe 600Pixel

```html
<!DOCTYPE html>
<html lang="de">
<head>
<meta charset="utf-8">
<title>Quarvelon – Startseite</title>
<link href="https://fonts.googleapis.com/css2?family=Lato:wght@400;700;900&family=Source+Sans+3:ital,wght@0,400;0,600;1,300&display=swap" rel="stylesheet">
<style>
  :root {
    --pink: #ef4a8c;
    --pink-dark: #b8346a;
    --pink-soft: #f78fb6;
    --slate: #2f3b41;
    --text: #3a4246;
    --page: #f7f7f7;
    --white: #ffffff;
    --hero-top: #7d5a58;
    --hero-mid: #6e5760;
    --hero-bottom: #5b6178;
  }
  * { margin: 0; padding: 0; box-sizing: border-box; }
  html, body { width: 1200px; height: 606px; overflow: hidden; background: var(--page); }
  body { position: relative; font-family: "Source Sans 3", "Calibri", sans-serif; color: var(--text); }

  .hero {
    position: absolute; left: 0; top: 0; width: 1200px; height: 481px;
    background: linear-gradient(180deg, var(--hero-top) 0%, var(--hero-mid) 45%, var(--hero-bottom) 100%);
  }
  .site-header { position: absolute; left: 0; top: 0; width: 1200px; height: 50px; }
  .brand {
    position: absolute; left: 190px; top: 11px;
    font-family: "Lato", sans-serif; font-weight: 700; font-size: 19px; color: var(--white);
  }
  .main-nav {
    position: absolute; right: 229px; top: 17px; display: flex; gap: 14px;
    font-family: "Lato", sans-serif; font-size: 9px; color: var(--white);
  }

  .slide {
    position: absolute; left: 184px; top: 80px; width: 788px; height: 361px;
    background: var(--white); overflow: hidden;
    box-shadow: 0 6px 14px rgba(0,0,0,0.45);
  }
  .slide-ring { position: absolute; left: 0; top: 0; }
  .slide-photo {
    position: absolute; right: 0; top: 0; width: 420px; height: 361px;
    background: linear-gradient(90deg, rgba(255,255,255,0) 0%, #e4e8e6 45%, #b9bfbd 100%);
  }
  .slide-photo::after {
    content: ""; position: absolute; right: 30px; top: 0; width: 230px; height: 330px;
    background: radial-gradient(ellipse at 55% 55%, #4a4443 0%, #5e5856 45%, rgba(94,88,86,0) 72%);
  }
  .quote {
    position: absolute; left: 68px; top: 108px;
    font-size: 31px; line-height: 42px; color: var(--text); font-weight: 400;
  }
  .quote-mark {
    position: absolute; font-family: "Source Sans 3", sans-serif; font-style: italic; font-weight: 600;
    font-size: 68px; line-height: 1; color: var(--pink);
  }
  .quote-mark.open { left: 26px; top: 108px; }
  .quote-mark.close { left: 371px; top: 126px; }
  .quote-author {
    position: absolute; right: 408px; top: 189px;
    font-style: italic; font-weight: 300; font-size: 13px; color: var(--text);
  }
  .slide-copy {
    position: absolute; left: 71px; top: 274px; font-size: 14px; line-height: 19px; color: var(--text);
  }
  .slide-copy strong { color: var(--pink); font-weight: 600; }
  .read-more {
    position: absolute; left: 69px; top: 319px; font-size: 18px; font-weight: 600;
    color: var(--pink); text-decoration: none;
  }
  .slide-brand {
    position: absolute; right: 20px; top: 336px; font-size: 17px; font-weight: 600; color: var(--text);
  }

  .slide-arrow {
    position: absolute; top: 236px; width: 33px; height: 49px; background: var(--pink);
    color: var(--white); font-family: "Lato", sans-serif; font-weight: 900; font-size: 26px;
    display: flex; align-items: center; justify-content: center;
  }
  .slide-arrow::before {
    content: ""; position: absolute; top: -12px; width: 0; height: 0;
  }
  .slide-arrow.prev { left: 174px; }
  .slide-arrow.prev::before { right: 23px; border-bottom: 12px solid var(--pink-dark); border-left: 10px solid transparent; }
  .slide-arrow.next { left: 949px; }
  .slide-arrow.next::before { left: 23px; border-bottom: 12px solid var(--pink-dark); border-right: 10px solid transparent; }

  .approach { position: absolute; left: 0; top: 481px; width: 1200px; height: 125px; background: var(--page); }
  .approach-title {
    position: absolute; left: 0; width: 1200px; top: 60px; text-align: center;
    font-family: "Lato", sans-serif; font-weight: 900; font-size: 30px; letter-spacing: -0.3px; color: var(--slate);
  }
  .approach-divider { position: absolute; left: 551px; top: 108px; }
</style>
</head>
<body>
  <section class="hero">
    <div class="hero-backdrop" role="img" aria-label="Getöntes Hintergrundfoto mit Konstruktionsplan und Rasterlinien" style="position:absolute;inset:0;"></div>

    <header class="site-header">
      <div class="brand">Quarvelon</div>
      <nav class="main-nav">
        <span>Home</span><span>Unser Ansatz</span><span>Produkte</span><span>Dienstleistungen</span><span>Schulungen</span>
      </nav>
    </header>

    <article class="slide">
      <svg class="slide-ring" width="200" height="80" viewBox="0 0 200 80" aria-hidden="true">
        <path d="M0 0 H172 A69 69 0 0 1 0 51 Z M34 0 A34 34 0 0 0 102 0 Z" fill="var(--pink-soft)" fill-rule="evenodd"/>
        <circle cx="68" cy="-3" r="34" fill="var(--white)"/>
      </svg>
      <div class="slide-photo" role="img" aria-label="Foto: Beine in schwarzen Lederschuhen, entspannt übereinandergeschlagen"></div>

      <span class="quote-mark open">„</span>
      <blockquote class="quote">Systemdiagnostik ist<br>unsere Leidenschaft.</blockquote>
      <span class="quote-mark close">”</span>
      <p class="quote-author">Lutz Wendel, CEO</p>

      <p class="slide-copy">Unsere Erfahrungen sind ganz klar: die Lösung, die Sie suchen,<br>darf die Kompelxität nicht zusäzlich erhöhen. Sie muss <strong>einfach</strong> sein.</p>
      <a class="read-more" href="#">&gt;&gt; Lesen Sie mehr</a>
      <div class="slide-brand">Quarvelon</div>
    </article>

    <div class="slide-arrow prev">&lt;</div>
    <div class="slide-arrow next">&gt;</div>
  </section>

  <section class="approach">
    <h2 class="approach-title">UNSER ANSATZ</h2>
    <svg class="approach-divider" width="50" height="12" viewBox="0 0 50 12" aria-hidden="true">
      <g stroke="var(--slate)" stroke-width="2.6" stroke-linecap="round">
        <path d="M2 2 L10 10 M10 2 L2 10"/>
        <path d="M20 2 L28 10 M28 2 L20 10"/>
        <path d="M38 2 L46 10 M46 2 L38 10"/>
      </g>
    </svg>
  </section>
</body>
</html>
```